New website for Pollard Law Firm at www.keepwinning-example.com

We are a professional law firm located in the Nashville, Tennessee USA area. We focus on personal injury law. We are looking for a slick new website that is user friendly for updating with new blogs, videos, etc. The primary colors should be red, black, and white. It should load extremely fast and have a good mobile component. The pages for the design will include a home page, about us, news, contact us, and practice page. The practice page will be copied for all the practice areas including motor vehicle accidents, slip and fall accidents, dog bites, etc. We have included an image which we would like to include in the new site which shows the color scheme The image is called banner-Car Wreck. The new website should NOT have gavels, court houses, law books, scales or the typical images for a law firm.

Target Market(s)

People in Tennessee involved in accidents

Industry/Entity Type

Legal services, law firm

Coding

Coded - Design and coding required

Number of Pages Required

5+ page

Font styles to use
Serif

Colors
EB3D1F
EC4F4E
F09395
F8D3D4
FCEDEE

Requirements
Should not have
• Gavels, columns, scales, law related images

```html
<!DOCTYPE html>
<html lang="en">
<head>
<meta charset="utf-8">
<title>Pollard Law Firm</title>
<link href="https://fonts.googleapis.com/css2?family=Playfair+Display:wght@400;500&family=Poppins:wght@300;400;500;600;700&display=swap" rel="stylesheet">
<style>
:root{
  --red:#d42b2b;
  --red-dark:#b81f22;
  --ink:#1c1c1e;
  --dark:#222226;
  --text:#555;
  --muted:#888;
  --white:#fff;
  --line:#e6e6e6;
}
*{margin:0;padding:0;box-sizing:border-box}
html,body{width:1200px;height:4695px;overflow:hidden}
body{position:relative;background:var(--white);font-family:'Poppins',sans-serif;color:var(--ink)}
.abs{position:absolute}
.serif{font-family:'Playfair Display',serif;font-weight:400}
.eyebrow{font-size:10px;font-weight:600;color:var(--red);letter-spacing:.3px;text-transform:uppercase}

/* header */
.site-header{left:88px;top:18px;width:1023px;height:59px;background:var(--white);display:flex;align-items:center;padding:0 28px;box-shadow:0 4px 14px rgba(0,0,0,.12);z-index:5}
.brand{font-family:'Playfair Display',serif;font-size:24px;color:var(--red);letter-spacing:.5px}
.main-nav{margin-left:auto;display:flex;align-items:center;gap:28px;font-size:12px;font-weight:500}
.main-nav .home{width:16px;height:16px}
.call{display:flex;align-items:center;gap:8px;margin-left:30px}
.call small{display:block;font-size:8px;color:var(--muted);font-weight:600}
.call strong{font-size:16px;font-weight:600}

/* hero */
.hero-photo{left:0;top:0;width:1200px;height:830px;background:linear-gradient(180deg,#3a4f6b 0%,#5a6478 35%,#8a5a3e 62%,#3b3540 80%,#1d2030 100%)}
.hero-photo::after{content:"";position:absolute;inset:0;background:rgba(0,0,0,.25)}
.hero-text{left:0;top:322px;width:1200px;text-align:center;color:var(--white);z-index:2}
.hero-text .eyebrow{font-size:11px}
.hero-text h1{font-size:64px;line-height:62px;margin-top:14px}
.hero-text p{font-size:16px;margin-top:22px}
.btn-red{display:inline-block;background:var(--red);color:var(--white);font-size:13px;font-weight:600;letter-spacing:.5px;padding:13px 24px;margin-top:16px}

/* about */
.about-frame{left:117px;top:1098px;width:306px;height:317px;border:4px solid var(--red)}
.about-photo{left:166px;top:903px;width:367px;height:460px;background:linear-gradient(160deg,#f2f2f4,#d9dbe0 60%,#2b2f3a 100%);box-shadow:0 20px 40px rgba(0,0,0,.18)}
.about-copy{left:618px;top:1000px;width:470px}
.about-copy h2{font-size:40px;margin-top:6px}
.about-copy .lead{font-size:14px;font-weight:500;margin-top:8px}
.about-copy .body{font-size:12px;line-height:22px;color:var(--text);margin-top:24px}
.btn-dark{left:963px;top:1300px;width:237px;height:62px;background:var(--ink);color:var(--white);padding:14px 0 0 38px}
.btn-dark small{display:block;font-size:9px;font-weight:600}
.btn-dark strong{font-size:19px;font-weight:600;letter-spacing:.5px}
.btn-dark svg{position:absolute;right:22px;top:23px}

/* practice */
.practice-band{left:788px;top:1506px;width:412px;height:595px;background:var(--red)}
.practice-head{left:84px;top:1745px}
.practice-head h2{font-size:40px;margin-top:4px}
.pager{left:88px;top:1838px;display:flex;gap:12px}
.pager span{width:38px;height:38px;border:1px solid var(--ink);display:flex;align-items:center;justify-content:center}
.pager span.on{background:var(--ink)}
.card{top:1627px;width:248px;height:352px;background:var(--white);box-shadow:0 6px 20px rgba(0,0,0,.1)}
.card .ph{height:211px}
.card .cb{padding:30px 24px}
.card h3{font-size:13px;font-weight:600}
.card p{font-size:12px;line-height:19px;color:var(--text);margin-top:6px}
.card a{display:inline-block;font-size:10px;font-weight:700;color:var(--red);text-decoration:underline;margin-top:10px}

/* video */
.video{left:0;top:2065px}
.video-title{left:0;top:2425px;width:1200px;text-align:center;color:var(--white);font-size:56px}

/* testimonials */
.quote{left:86px;top:2895px}
.testi{left:88px;top:2966px;width:520px}
.testi h2{font-size:40px;margin-top:6px}
.testi .body{font-size:13px;line-height:22px;color:var(--text);margin-top:16px}
.testi .name{font-size:20px;font-weight:600;color:var(--red);margin-top:14px}
.testi .role{font-size:16px}
.round-arrows{left:90px;top:3268px;display:flex;gap:10px}
.round-arrows span{width:38px;height:38px;border-radius:50%;background:#f3f3f3;display:flex;align-items:center;justify-content:center}

/* news */
.news-head{left:0;top:3386px;width:1200px;text-align:center}
.news-head h2{font-size:40px;margin-top:4px}
.post{top:3484px;width:328px;height:429px;background:var(--white);box-shadow:0 6px 22px rgba(0,0,0,.09)}
.post .ph{height:246px}
.post .pb{padding:28px 30px}
.post .meta{font-size:12px;color:var(--red)}
.post h3{font-size:15px;font-weight:600;line-height:22px;margin-top:10px;text-transform:uppercase}
.post p{font-size:13.5px;line-height:21px;color:var(--text);margin-top:8px}

/* appointment + footer */
.appt-text{left:143px;top:4075px;width:570px;color:var(--white)}
.appt-text h2{font-size:46px}
.appt-text p{font-size:12px;line-height:20px;margin-top:4px}
.btn-white{left:784px;top:4108px;width:226px;height:56px;background:var(--white);color:var(--ink);font-size:20px;font-weight:700;display:flex;align-items:center;justify-content:center;letter-spacing:.5px}
.footer-brand{left:88px;top:4450px;font-family:'Playfair Display',serif;font-size:32px;color:var(--red)}
.fcol{top:4366px;color:var(--white)}
.fcol h4{font-size:18px;font-weight:600}
.fcol ul{list-style:none;margin-top:22px}
.fcol li{font-size:12px;margin-bottom:14px}
.fcol p{font-size:12px;line-height:18px}
.subscribe{margin-top:14px;width:260px;height:42px;background:#3a3a3f;display:flex;align-items:center;justify-content:space-between;padding:0 18px;font-size:11px}
.contact-row{display:flex;gap:10px;font-size:12px;line-height:22px;margin-top:6px}
.footer-rule{left:88px;top:4633px;width:1023px;height:1px;background:#3b3b40}
.copyright{left:88px;top:4662px;font-size:10px;font-weight:600;color:var(--white)}
.socials{left:972px;top:4662px;display:flex;gap:24px}
.socials span{width:12px;height:12px;border-radius:50%;background:var(--white)}
.to-top{left:1142px;top:4622px;width:36px;height:36px;border-radius:50%;background:var(--red);display:flex;align-items:center;justify-content:center}
</style>
</head>
<body>

<!-- header -->
<header class="abs site-header">
  <div class="brand">Pollard Law Firm</div>
  <nav class="main-nav">
    <svg class="home" viewBox="0 0 16 16"><path d="M8 1 1 8h2v6h4v-4h2v4h4V8h2z" fill="#d42b2b"/></svg>
    <span>ABOUT US</span><span>PRACTICES</span><span>NEWS</span><span>CONTACT US</span>
  </nav>
  <div class="call">
    <svg width="20" height="20" viewBox="0 0 24 24"><path d="M6.6 10.8a15 15 0 0 0 6.6 6.6l2.2-2.2a1 1 0 0 1 1-.25 11 11 0 0 0 3.6.6 1 1 0 0 1 1 1V20a1 1 0 0 1-1 1A17 17 0 0 1 3 4a1 1 0 0 1 1-1h3.5a1 1 0 0 1 1 1 11 11 0 0 0 .6 3.6 1 1 0 0 1-.25 1z" fill="#d42b2b"/></svg>
    <div><small>CALL NOW</small><strong>(615) 555-0142</strong></div>
  </div>
</header>

<!-- hero -->
<section>
  <div class="abs hero-photo" role="img" aria-label="City skyline at dusk with river reflections"></div>
  <svg class="abs" style="left:0;top:690px;z-index:3" width="1200" height="150">
    <polygon points="0,95 1200,15 1200,38 0,132" fill="#d42b2b"/>
    <polygon points="0,132 1200,38 1200,150 0,150" fill="#fff"/>
  </svg>
  <div class="abs hero-text">
    <div class="eyebrow">Pollard Law Firm PLLC</div>
    <h1 class="serif">Don’t lose<br>what’s legally yours</h1>
    <p>We are trial lawyers and we are proud of it!</p>
    <span class="btn-red">PRACTICE AREAS</span>
  </div>
</section>

<!-- about -->
<section>
  <div class="abs about-frame"></div>
  <div class="abs about-photo" role="img" aria-label="Portrait of the firm's lead attorney in a suit"></div>
  <div class="abs about-copy">
    <div class="eyebrow">About us</div>
    <h2 class="serif">Trial Lawyers...</h2>
    <p class="lead">We are trial lawyers and we are proud of it!</p>
    <p class="body">WE ARE TRIAL LAWYERS AND WE ARE PROUD OF IT! There are many law firms in Tennessee who claim to be trial lawyers, but their attorneys have never seen a courtroom. We have tried hundreds of cases to verdict and we have helped thousands of people in the Tennessee courts. We fight against billion dollar insurance companies, billion dollar corporations, and the State of Tennessee..and we win!</p>
  </div>
  <div class="abs btn-dark"><small>LEARN MORE</small><strong>ABOUT US</strong>
    <svg width="22" height="14" viewBox="0 0 22 14"><path d="M0 7h20M14 1l6 6-6 6" stroke="#fff" stroke-width="1.5" fill="none"/></svg></div>
</section>

<!-- practice areas -->
<section>
  <div class="abs practice-band" role="img" aria-label="Red tinted background photo"></div>
  <div class="abs practice-head"><div class="eyebrow">Services</div><h2 class="serif">Practice Areas</h2></div>
  <div class="abs pager">
    <span><svg width="8" height="10"><path d="M6 1 2 5l4 4" stroke="#1c1c1e" stroke-width="1.5" fill="none"/></svg></span>
    <span class="on"><svg width="8" height="10"><path d="m2 1 4 4-4 4" stroke="#fff" stroke-width="1.5" fill="none"/></svg></span>
  </div>
  <article class="abs card" style="left:440px">
    <div class="ph" role="img" aria-label="Paramedic helping an injured person" style="background:linear-gradient(135deg,#c9402e,#8a8e96 60%,#3b3f48)"></div>
    <div class="cb"><h3>PERSONAL INJURY</h3><p>Lorem quis bibendum auctor, nisi elit consequat .</p><a>LEARN MORE</a></div>
  </article>
  <article class="abs card" style="left:699px">
    <div class="ph" role="img" aria-label="Wet floor sign beside a person who slipped" style="background:linear-gradient(135deg,#e8e8ea,#c8cacd 60%,#e0b530)"></div>
    <div class="cb"><h3>SLIP AND FALL ACCIDENT</h3><p>Lorem quis bibendum auctor, nisi elit consequat .</p><a>LEARN MORE</a></div>
  </article>
  <article class="abs card" style="left:958px">
    <div class="ph" role="img" aria-label="Children playing with a dog outdoors" style="background:linear-gradient(135deg,#7f9a58,#d3473f 55%,#c9b08a)"></div>
    <div class="cb"><h3>DOG BITES</h3><p>Lorem quis bibendum auctor, nisi elit consequat .</p><a>LEARN MORE</a></div>
  </article>
</section>

<!-- video -->
<svg class="abs video" width="1200" height="660" role="img" aria-label="Car accident scene with an injured person on the road">
  <defs><linearGradient id="vg" x1="0" y1="0" x2="1" y2="1"><stop offset="0" stop-color="#4a4e55"/><stop offset=".5" stop-color="#6b6d70"/><stop offset="1" stop-color="#3a3b3e"/></linearGradient></defs>
  <polygon points="0,105 1200,2 1200,543 0,653" fill="url(#vg)"/>
  <polygon points="0,105 1200,2 1200,543 0,653" fill="rgba(0,0,0,.2)"/>
  <circle cx="613" cy="293" r="55" fill="#fff"/>
  <polygon points="603,275 603,311 631,293" fill="#d42b2b"/>
</svg>
<div class="abs video-title serif">Watch Video</div>

<!-- testimonials -->
<section>
  <svg class="abs quote" width="94" height="64" viewBox="0 0 94 64"><path d="M0 64V36C0 14 10 3 30 0l4 8C22 12 18 20 18 30h16v34zm52 0V36c0-22 10-33 30-36l4 8c-12 4-16 12-16 22h14v34z" fill="#eee"/></svg>
  <div class="abs testi">
    <div class="eyebrow">Testimonials</div>
    <h2 class="serif">What Our Client Say</h2>
    <p class="body">Lorem Ipsum is simply dummy text of the printing and typesetting industry. Lorem Ipsum has been the industry's standard dummy text ever since the 1500s, when an unknown printer took a galley of type and scrambled it to make a type specimen book. It has survived not only five centuries, but also the leap into electronic typesetting, remaining essentially unchanged. It was popularised</p>
    <div class="name">John Smith</div>
    <div class="role">Co Founder</div>
  </div>
  <div class="abs round-arrows">
    <span><svg width="12" height="10"><path d="M11 5H1m4-4L1 5l4 4" stroke="#333" fill="none"/></svg></span>
    <span><svg width="12" height="10"><path d="M1 5h10M7 1l4 4-4 4" stroke="#333" fill="none"/></svg></span>
  </div>
  <svg class="abs" style="left:660px;top:2780px" width="540" height="600">
    <g fill="none" stroke="#e6e6e6" stroke-width="2">
      <circle cx="298" cy="297" r="278"/><circle cx="298" cy="297" r="173"/><circle cx="298" cy="297" r="73"/>
    </g>
    <g role="img" aria-label="Client portraits">
      <circle cx="130" cy="212" r="84" fill="#b9bec6" stroke="#fff" stroke-width="6"/>
      <circle cx="298" cy="396" r="62" fill="#8c6b58" stroke="#fff" stroke-width="5"/>
      <circle cx="451" cy="320" r="50" fill="#6f564a" stroke="#fff" stroke-width="5"/>
      <circle cx="130" cy="350" r="34" fill="#7c8a5e" stroke="#fff" stroke-width="4"/>
      <circle cx="298" cy="218" r="28" fill="#c7b3a6" stroke="#fff" stroke-width="4"/>
      <circle cx="130" cy="52" r="20" fill="#6a6e78" stroke="#fff" stroke-width="4"/>
      <circle cx="372" cy="96" r="18" fill="#8d8f96" stroke="#fff" stroke-width="4"/>
      <circle cx="112" cy="475" r="18" fill="#b48c80" stroke="#fff" stroke-width="4"/>
      <circle cx="392" cy="524" r="30" fill="#5d7086" stroke="#fff" stroke-width="4"/>
    </g>
  </svg>
</section>

<!-- news -->
<section>
  <div class="abs news-head"><div class="eyebrow">News</div><h2 class="serif">The Latest from Pollard</h2></div>
  <article class="abs post" style="left:88px">
    <div class="ph" role="img" aria-label="Semi truck and car on a highway" style="background:linear-gradient(180deg,#6e8bb0,#c9c6c0 55%,#4a4a4e)"></div>
    <div class="pb"><div class="meta">July 1, 2019</div><h3>Trucking company offers 6 figure settlement</h3><p>On a Thursday afternoon, our client was traveling to work...</p></div>
  </article>
  <article class="abs post" style="left:434px">
    <div class="ph" role="img" aria-label="Medical bill paperwork with a stethoscope" style="background:linear-gradient(135deg,#e9e9eb,#cfd0d3 55%,#c9333a)"></div>
    <div class="pb"><div class="meta">October 1, 2018 &nbsp;•&nbsp; law, personal injury</div><h3>Pollard obtains jury verdict of 61 x medical bills</h3><p>In 2016, a client was traveling down a road and stopped in traffic</p></div>
  </article>
  <article class="abs post" style="left:781px">
    <div class="ph" role="img" aria-label="Hands signing an insurance policy" style="background:linear-gradient(135deg,#2a2a2c,#e5e5e5 50%,#2d2d30)"></div>
    <div class="pb"><div class="meta">August 1, 2018 &nbsp;•&nbsp; personal injury</div><h3>Insurance company pays for facial fractures</h3><p>On a dark night in Murfreesboro, Tennessee, a young woman</p></div>
  </article>
</section>

<!-- appointment & footer -->
<svg class="abs" style="left:0;top:4016px" width="1200" height="679">
  <polygon points="0,158 1200,88 1200,679 0,679" fill="#222226"/>
  <polygon points="88,0 1109,0 1030,221 88,221" fill="#d42b2b"/>
</svg>
<div class="abs appt-text">
  <h2 class="serif">Book An Appointment</h2>
  <p>Use the form below to tell us about your legal inquiry, and we’ll call you back to schedule an appointment. Please be as detailed as possible. Include what industry you need service for along...</p>
</div>
<div class="abs btn-white">BOOK NOW</div>

<div class="abs footer-brand">Pollard Law Firm</div>
<div class="abs fcol" style="left:410px">
  <h4>Quick Links</h4>
  <ul><li>Home</li><li>About us</li><li>Practices Areas</li><li>News</li><li>Contact us</li></ul>
</div>
<div class="abs fcol" style="left:593px;width:270px">
  <h4>Newsletter</h4>
  <p style="margin-top:22px">Subscribe to our email address to get the latest news.</p>
  <div class="subscribe"><span>Enter Your Email...</span>
    <svg width="14" height="14" viewBox="0 0 14 14"><path d="M13 1 1 6l5 2 2 5z" fill="#d42b2b"/></svg></div>
</div>
<div class="abs fcol" style="left:903px;width:220px">
  <h4>Contact info</h4>
  <div style="margin-top:14px">
    <div class="contact-row"><svg width="12" height="22" viewBox="0 0 12 22"><rect x="0" y="7" width="12" height="9" fill="#d42b2b"/></svg><span>office@pollardlaw-example.com</span></div>
    <div class="contact-row"><svg width="12" height="22" viewBox="0 0 12 22"><circle cx="6" cy="11" r="5" fill="#d42b2b"/></svg><span>(615) 555-0142</span></div>
    <div class="contact-row"><svg width="12" height="22" viewBox="0 0 12 22"><path d="M6 4a4 4 0 0 1 4 4c0 3-4 8-4 8S2 11 2 8a4 4 0 0 1 4-4z" fill="#d42b2b"/></svg><span>1450 Maple Crest Drive<br>Suite 210, Harbor Square<br>Franklin, TN 37064</span></div>
  </div>
</div>
<div class="abs footer-rule"></div>
<div class="abs copyright">©2021 POLLARD LAW FIRM, PLLC. ALL RIGHTS RESERVED.</div>
<div class="abs socials"><span></span><span></span><span></span><span></span></div>
<div class="abs to-top"><svg width="10" height="12"><path d="M5 11V1M1 5l4-4 4 4" stroke="#fff" fill="none"/></svg></div>

</body>
</html>
```